Harlow Stonefield Civil Construction website design

We want a Bold website to promote our Heavy Civil Construction company, We would like an organic / tangible feel to the site. The pictures will be over saturated so they pop. We need to be able to easliy upload new projects and pictures on a regular basis.
Home page will have a full screen width image, "home page image" with silhouette and logo. It will also have about us area and picture
Page 2 will be Project Gallery with pictures in project folders
Page 3 will be an employment application form and submission
Page 4 will be Contact Us
Target Market(s)
Construction indusrty
Industry/Entity Type
Contractor
Coding
Coded - Design and coding required
Number of Pages Required
4 page
Font styles to use
Other font styles liked:
- Hypatia Sans Pro Light
Look and feel

```html
<!DOCTYPE html>
<html lang="en">
<head>
<meta charset="utf-8">
<title>Harlow Stonefield Civil Construction</title>
<link rel="stylesheet" href="https://fonts.googleapis.com/css2?family=Alegreya+Sans:wght@300;400;500;700&family=Josefin+Sans:wght@600;700&family=Oswald:wght@400;500&display=swap">
<style>
:root{
  --blue:#2e48a6;
  --blue-deep:#26408f;
  --yellow:#f2cf1d;
  --panel:#f2f3f7;
  --field:#eff0f2;
  --ink:#3b3e48;
  --muted:#666a73;
  --white:#ffffff;
  --body:"Alegreya Sans",sans-serif;
  --caps:"Josefin Sans",sans-serif;
}
*{box-sizing:border-box;margin:0;padding:0}
html,body{width:1200px;height:2663px;overflow:hidden}
body{position:relative;background:var(--white);font-family:var(--body);color:var(--ink)}
.abs{position:absolute}

/* header */
.brand{left:0;top:0;width:350px;height:97px;background:var(--white);display:flex;align-items:center;padding-left:40px;gap:12px}
.brand-mark{width:44px;height:44px;border:3px solid var(--blue)}
.brand-name{font-family:var(--body);font-weight:700;font-size:21px;line-height:1.05;color:var(--blue);text-transform:uppercase;letter-spacing:.5px}
.topbar{left:350px;top:0;width:850px;height:97px;background:var(--blue)}
.nav a{position:absolute;top:41px;font-family:var(--caps);font-weight:700;font-size:11.5px;letter-spacing:1px;color:var(--white);text-decoration:none;text-transform:uppercase}
.nav a.active{color:var(--yellow)}
.call{left:875px;top:34px;font-family:"Oswald",sans-serif;font-size:17px;color:var(--white)}
.call span{color:var(--yellow)}
.social{display:flex;gap:10px}
.social i{display:block;width:32px;height:32px;border-radius:50%;border:2px solid var(--yellow)}
.social i.on{background:var(--yellow)}

/* hero */
.hero{left:0;top:97px;width:1200px;height:551px;background:linear-gradient(180deg,#5f6670 0%,#4d535c 40%,#2a2d31 72%,#08090a 100%)}
.hero-title{left:0;top:258px;width:1200px;text-align:center;color:var(--white)}
.hero-title h1{font-weight:500;font-size:39px;letter-spacing:2px;line-height:1}
.hero-title p{font-weight:300;font-size:31px;letter-spacing:1px;margin-top:6px;text-transform:uppercase}
.arrow{top:316px;width:24px;height:24px}
.btn{display:flex;align-items:center;justify-content:center;background:var(--yellow);border-radius:18px;font-family:var(--caps);font-weight:700;font-size:11px;letter-spacing:1.2px;color:var(--blue-deep);text-transform:uppercase}
.btn.ghost{background:var(--white);border:2px solid var(--yellow)}

/* about */
.about-panel{left:0;top:648px;width:600px;height:445px;background:var(--panel)}
.section-title{display:flex;align-items:center;gap:22px;font-weight:500;font-size:32px;text-transform:uppercase;color:var(--blue);letter-spacing:.5px}
.section-title span{color:#555b6a;font-weight:400}
.section-title::after{content:"";display:block;width:80px;height:2px;background:var(--blue)}
.about-copy{left:82px;top:773px;width:425px;font-size:13.5px;line-height:20px;color:var(--muted)}
.about-copy p+p{margin-top:20px}
.about-photo{left:600px;top:648px;width:600px;height:445px;background:linear-gradient(180deg,#6aa6e8 0%,#8fbde8 25%,#5a7a3c 40%,#8c8a82 62%,#a9a8a4 100%)}
.badge{left:572px;top:831px;width:68px;height:78px;background:var(--white);border-radius:6px;box-shadow:0 4px 12px rgba(0,0,0,.18)}

/* projects */
.filters{left:520px;top:1181px;width:598px;text-align:right;font-family:var(--caps);font-weight:600;font-size:9px;letter-spacing:.8px;color:#9a9ea8;text-transform:uppercase}
.filters b{color:var(--blue);font-weight:700}
.filters em{font-style:normal;margin:0 8px}
.card{width:502px;height:284px}
.card h3{position:absolute;left:32px;bottom:26px;font-family:var(--caps);font-weight:700;font-size:13px;letter-spacing:1.2px;color:var(--white);text-transform:uppercase}
.card p{position:absolute;left:32px;bottom:34px;width:420px;font-size:13.5px;line-height:20px;color:#e6e8ee}
.card.featured h3{bottom:92px}
.c1{left:82px;top:1235px;background:linear-gradient(180deg,#55657a 0%,#7c8087 45%,#c9ccd0 80%,#9a9b96 100%)}
.c2{left:616px;top:1235px;background:linear-gradient(180deg,#3e5576 0%,#53657c 55%,#2f3a2a 100%)}
.c3{left:82px;top:1553px;background:linear-gradient(180deg,#6f7a68 0%,#5c7351 45%,#887f6c 75%,#3f5a4a 100%)}
.c4{left:616px;top:1553px;background:linear-gradient(180deg,#59718b 0%,#5d6a70 40%,#6e6a60 70%,#3b3d36 100%)}

/* hiring */
.hiring{left:0;top:1990px;width:1200px;height:161px;background:linear-gradient(90deg,#3450b0 0%,#2e48a6 60%,#3853ae 100%)}
.hiring h2{position:absolute;left:80px;top:60px;font-weight:300;font-size:34px;color:var(--white)}

/* contact */
.label{font-weight:700;font-size:12.5px;letter-spacing:.3px;text-transform:uppercase;color:var(--ink)}
.phone{left:80px;top:2322px;font-weight:300;font-size:43px;color:var(--blue)}
.mail{left:82px;top:2373px;font-size:14px;color:var(--muted)}
.mail b{color:var(--ink)}
.addr{left:82px;top:2446px;font-size:13px;line-height:23px;color:var(--muted)}
.field{background:var(--field);font-size:13px;color:#7a7e87;padding:12px 14px}
.send{left:1051px;top:2466px;width:42px;height:42px;border-radius:50%;background:var(--yellow)}
.copy{left:82px;top:2570px;font-size:13px;color:var(--ink)}
.copy span{color:var(--blue);font-family:var(--caps);font-weight:700;font-size:10.5px;letter-spacing:.5px}
.social.blue i{border-color:var(--blue);width:30px;height:30px}
.social.blue i.on{background:var(--blue)}
</style>
</head>
<body>

<header>
  <div class="abs brand">
    <div class="brand-mark"></div>
    <div class="brand-name">Harlow Stonefield<br>Civil Construction</div>
  </div>
  <div class="abs topbar"></div>
  <nav class="nav">
    <a class="active" href="#" style="left:424px">- Home -</a>
    <a href="#" style="left:510px">About Us</a>
    <a href="#" style="left:602px">Gallery</a>
    <a href="#" style="left:684px">Career</a>
    <a href="#" style="left:760px">Contact Us</a>
  </nav>
  <div class="abs call"><span>Call Us:</span> 123-456-7890</div>
  <div class="abs social" style="left:1045px;top:32px"><i></i><i class="on"></i><i></i></div>
</header>

<section>
  <div class="abs hero" role="img" aria-label="Silhouettes of an excavator and heavy machines against a grey evening sky"></div>
  <div class="abs hero-title">
    <h1>HARLOW STONEFIELD</h1>
    <p>Heavy Civil Construction Company</p>
  </div>
  <svg class="abs arrow" style="left:77px" viewBox="0 0 24 24"><path d="M15 4 7 12l8 8" fill="none" stroke="#fff" stroke-width="2"/></svg>
  <svg class="abs arrow" style="left:1099px" viewBox="0 0 24 24"><path d="m9 4 8 8-8 8" fill="none" stroke="#fff" stroke-width="2"/></svg>
  <a class="abs btn" style="left:536px;top:367px;width:128px;height:33px">Contact Us</a>
</section>

<section>
  <div class="abs about-panel"></div>
  <h2 class="abs section-title" style="left:82px;top:720px">About<span>Us</span></h2>
  <div class="abs about-copy">
    <p>Harlow Stonefield is a heavy civil construction company. It is a long established fact that a reader will be distracted by the readable content of a page when looking at its layout. The point of using Lorem Ipsum is that it has a more-or-less normal distribution of letters, as opposed to using 'Content here.</p>
    <p>making it look like readable English. Many desktop publishing packages and web page editors now use Lorem Ipsum as their default model text, and a search for 'lorem ipsum ...</p>
  </div>
  <a class="abs btn ghost" style="left:82px;top:977px;width:130px;height:32px">Explore More</a>
  <div class="abs about-photo" role="img" aria-label="Yellow long-reach excavator working on a retaining wall site under blue sky"></div>
  <div class="abs badge"></div>
</section>

<section>
  <h2 class="abs section-title" style="left:82px;top:1166px">Our<span>Projects</span></h2>
  <div class="abs filters"><b>All</b><em>/</em>Marine Construction<em>/</em>Excavation &amp; Grading<em>/</em>Land Development<em>/</em>Underground Utilities</div>

  <div class="abs card c1" role="img" aria-label="Steel structure above a shoreline covered with geotextile"><h3>Marine Construction</h3></div>
  <div class="abs card c2 featured" role="img" aria-label="Yellow excavator under a cloudy sky"><h3>Excavation and Grading</h3><p>There are many variations of passages of Lorem Ipsum available, but the majority have suffered alteration</p></div>
  <div class="abs card c3" role="img" aria-label="Aerial view of a land development site near a pond"><h3>Land Development</h3></div>
  <div class="abs card c4" role="img" aria-label="Dirt mounds on an underground utilities site with a rainbow"><h3>Underground Utilities</h3></div>

  <a class="abs btn" style="left:527px;top:1877px;width:146px;height:32px">View All Work</a>
</section>

<section class="abs hiring" role="img" aria-label="Blue toned construction site landscape">
  <h2>We Are Hiring for Various Positions.</h2>
  <a class="abs btn" style="left:834px;top:65px;width:284px;height:33px">Employment Application Form</a>
</section>

<section>
  <h2 class="abs section-title" style="left:82px;top:2226px">Contact<span>Us</span></h2>
  <div class="abs label" style="left:82px;top:2295px">Need Help? Call Us</div>
  <div class="abs phone">+123-456-7890</div>
  <div class="abs mail"><b>E:.</b> info@harlowstonefield.com</div>
  <div class="abs label" style="left:82px;top:2416px">Address</div>
  <div class="abs addr">P.O Box 690, Lorem ipsum House, 1685 4 Ipsum Street,<br>Design, Lorem, 1234</div>

  <div class="abs field" style="left:616px;top:2235px;width:243px;height:40px">Name</div>
  <div class="abs field" style="left:875px;top:2235px;width:243px;height:40px">Phone</div>
  <div class="abs field" style="left:616px;top:2293px;width:502px;height:41px">Email</div>
  <div class="abs field" style="left:616px;top:2352px;width:502px;height:133px">Message</div>
  <div class="abs send"><svg width="42" height="42" viewBox="0 0 42 42"><path d="M14 14 29 21 14 28l2-7z" fill="var(--blue-deep)"/></svg></div>

  <div class="abs copy">© 2019 <span>HARLOW STONEFIELD CIVIL CONSTRUCTION.</span> All Right Rreserved</div>
  <div class="abs social blue" style="left:1006px;top:2564px"><i></i><i class="on"></i><i></i></div>
</section>

</body>
</html>
```